New Project to be launched in Canada . The Electronic Shelf Label (ESL).Provide you real-time price adjustment, enhanced user experience and an intelligent marketing assistant.

product advantage :
1)Provide you real-time price adjustment,
2)enhanced user experience and an intelligent marketing assistant ,
3) ROI on investment within 2 -3 years
4)different colors can be used to indicate the status of each commodity (picking, on sale, out of stock, etc).

5) multiple sizes:
1) 2.13 inch BWR
2) 2.6 inch BWR
3) 2.6 inch Anti freezing -20 c
4)4.2 inch
5) 4.2 inch dustproof, waterproof
6)7.5 inch

Epaper display
Led Color 7 color
Battery level 3 years
OTA support

```html
<!DOCTYPE html>
<html lang="en">
<head>
<meta charset="utf-8">
<title>Electronic Shelf Label ESL</title>
<link href="https://fonts.googleapis.com/css2?family=Archivo+Black&family=Montserrat:wght@500;600;700&display=swap" rel="stylesheet">
<style>
  :root {
    --brand-blue: #3f6db5;
    --brand-green: #8dc63f;
    --text-grey: #5a5a5a;
    --page-white: #ffffff;
    --haze: #f6f6f4;
    --tint-green-light: #eef5d8;
    --tint-green-mid: #d7eab0;
  }
  * { margin: 0; padding: 0; box-sizing: border-box; }
  html, body { width: 1200px; height: 905px; overflow: hidden; background: var(--page-white); }
  .page {
    position: relative;
    width: 1200px;
    height: 905px;
    background: linear-gradient(180deg, var(--page-white) 0%, var(--haze) 35%, var(--page-white) 100%);
    font-family: "Montserrat", sans-serif;
  }
  .brand {
    position: absolute;
    left: 72px;
    top: 78px;
    display: flex;
    align-items: center;
    gap: 12px;
  }
  .brand-dot {
    width: 22px; height: 22px; border-radius: 50%;
    background: var(--brand-green);
  }
  .brand-name {
    font-family: "Montserrat", sans-serif;
    font-weight: 700;
    font-size: 40px;
    letter-spacing: 0.5px;
    color: var(--brand-blue);
  }
  .illustration {
    position: absolute;
    left: 0;
    top: 270px;
    width: 960px;
    height: 560px;
  }
  .headline {
    position: absolute;
    left: 586px;
    top: 168px;
    font-family: "Archivo Black", sans-serif;
    font-size: 57px;
    line-height: 58px;
    color: var(--brand-blue);
    letter-spacing: 0.5px;
  }
  .headline .accent { color: var(--brand-green); }
  .tagline {
    position: absolute;
    left: 586px;
    top: 326px;
    width: 520px;
    font-size: 18.5px;
    font-weight: 500;
    line-height: 23px;
    color: var(--text-grey);
  }
  .footer-band {
    position: absolute;
    left: 0;
    top: 834px;
    width: 1200px;
    height: 44px;
    background: var(--brand-blue);
    display: flex;
    align-items: center;
    padding-left: 108px;
    gap: 28px;
    color: var(--page-white);
    font-size: 22px;
    font-weight: 500;
    letter-spacing: 0.5px;
  }
  .page-number {
    position: absolute;
    left: 1131px;
    top: 818px;
    width: 38px; height: 38px;
    border-radius: 50%;
    background: var(--brand-green);
    border: 3px solid var(--page-white);
    color: var(--page-white);
    font-weight: 700;
    font-size: 20px;
    display: flex; align-items: center; justify-content: center;
  }
</style>
</head>
<body>
  <main class="page">
    <header class="brand">
      <span class="brand-dot"></span>
      <span class="brand-name">Norvale Payments</span>
    </header>

    <svg class="illustration" viewBox="0 0 960 560" role="img" aria-label="Isometric illustration of a central green server connected to three blue store fronts, each showing an electronic shelf price label">
      <defs>
        <linearGradient id="stageTint" x1="0" y1="0" x2="1" y2="1">
          <stop offset="0" stop-color="var(--tint-green-mid)"/>
          <stop offset="1" stop-color="var(--tint-green-light)"/>
        </linearGradient>
      </defs>
      <path d="M0 260 L400 30 Q430 14 460 30 L1000 330 Q1040 360 1000 390 L560 560 L0 560 Z" fill="url(#stageTint)" opacity="0.8"/>
    </svg>

    <h1 class="headline">ELECTRONIC<br>SHELF LABEL <span class="accent">ESL</span></h1>
    <p class="tagline">Provide you real-time price adjustment, enhanced user experience and an intelligent marketing assistant.</p>

    <footer class="footer-band">
      <span class="issue-month">MARCH</span>
      <span class="issue-year">2020</span>
    </footer>
    <div class="page-number">1</div>
  </main>
</body>
</html>
```